Business Card Design Project

We need a Business Card Design for our Architectural Company, we want the cards to stand out WOW factor, we are thinking to have the logo on the front and embossed and all the contact info etc on the back. however we are open to suggestions

Target Market(s)

Adults looking for a Architect for their design project, or a developers who need an architecture firm to partner with. Card should be very powerful and portray elegance and creativity as first impression

Industry/Entity Type

Business

Requirements
Must have
• Must have large logo and easy to read address info, current card attached for address and contact info that should be on card.

```html
<!DOCTYPE html>
<html lang="en">
<head>
<meta charset="utf-8">
<title>Seabright Design Group – Business Card</title>
<link rel="stylesheet" href="https://fonts.googleapis.com/css2?family=Montserrat:wght@700&family=Arimo:wght@400&family=Tinos:wght@400&display=swap">
<style>
  :root {
    --navy: #2e2a7a;
    --red: #d9261c;
    --swoosh: #3b3b3b;
    --ink: #1a1a1a;
    --grey-text: #333333;
    --paper: #ffffff;
    --backdrop: #8a8a8a;
    --rule: #9a9a9a;
  }
  * { margin: 0; padding: 0; box-sizing: border-box; }
  html, body { width: 1200px; height: 800px; overflow: hidden; }
  body { background: var(--backdrop); position: relative; }

  .card {
    position: absolute;
    width: 620px;
    height: 350px;
    background: var(--paper);
    overflow: hidden;
    box-shadow: 0 2px 6px rgba(0,0,0,0.25);
  }

  /* Front */
  .card-front { left: 80px; top: 50px; }
  .front-brand {
    position: absolute;
    left: 40px;
    top: 100px;
    display: flex;
    align-items: center;
    gap: 22px;
  }
  .brand-square {
    width: 96px;
    height: 96px;
    background: var(--navy);
  }
  .brand-name {
    font-family: "Montserrat", sans-serif;
    font-weight: 700;
    color: var(--navy);
    text-transform: uppercase;
    line-height: 1.08;
  }
  .front-brand .brand-name { font-size: 27px; }
  .front-rule {
    position: absolute;
    left: 0; right: 0;
    top: 222px;
    height: 2px;
    background: var(--navy);
  }
  .front-band {
    position: absolute;
    left: 0; right: 0;
    top: 230px;
    height: 38px;
    background: var(--navy);
  }

  /* Back */
  .card-back { left: 500px; top: 400px; }
  .back-shape { position: absolute; inset: 0; }
  .back-brand {
    position: absolute;
    left: 36px;
    top: 62px;
    display: flex;
    align-items: center;
    gap: 12px;
  }
  .back-brand .brand-square { width: 40px; height: 40px; }
  .back-brand .brand-name { font-size: 13px; }
  .person {
    position: absolute;
    left: 36px;
    top: 170px;
    width: 300px;
  }
  .person-name {
    font-family: "Arimo", sans-serif;
    font-size: 22px;
    color: var(--ink);
    padding-bottom: 4px;
    border-bottom: 1px solid var(--rule);
  }
  .person-title {
    font-family: "Arimo", sans-serif;
    font-size: 13px;
    color: var(--ink);
    margin-top: 6px;
  }
  .address {
    position: absolute;
    left: 36px;
    top: 250px;
    font-family: "Tinos", serif;
    font-size: 16px;
    line-height: 1.1;
    color: var(--grey-text);
    font-style: normal;
  }
  .contact-list {
    position: absolute;
    left: 440px;
    top: 178px;
    list-style: none;
    font-family: "Tinos", serif;
    font-size: 14px;
    color: var(--paper);
  }
  .contact-list li {
    display: flex;
    align-items: center;
    gap: 6px;
    height: 24px;
  }
  .contact-icon { width: 14px; height: 14px; flex: none; }
</style>
</head>
<body>

<section class="card card-front" aria-label="Card front">
  <div class="front-brand">
    <div class="brand-square"></div>
    <div class="brand-name">Seabright<br>Design<br>Group Ltd</div>
  </div>
  <div class="front-rule"></div>
  <div class="front-band"></div>
</section>

<section class="card card-back" aria-label="Card back">
  <svg class="back-shape" viewBox="0 0 620 350" width="620" height="350" aria-hidden="true">
    <path d="M400 0 C430 40 440 90 426 150 C412 220 430 300 472 350 L620 350 L620 0 Z" fill="var(--red)"/>
    <path d="M385 0 C420 40 428 90 414 150 C400 220 418 300 462 350" fill="none" stroke="var(--swoosh)" stroke-width="4"/>
    <path d="M392 0 C424 40 434 90 420 150 C406 220 424 300 467 350" fill="none" stroke="var(--paper)" stroke-width="2"/>
  </svg>

  <div class="back-brand">
    <div class="brand-square"></div>
    <div class="brand-name">Seabright Design<br>Group Ltd</div>
  </div>

  <div class="person">
    <div class="person-name">Marcus Reid</div>
    <div class="person-title">Managing Director</div>
  </div>

  <address class="address">
    Harbour Point, Unit #5<br>
    P.O. Box 40731<br>
    Grand Cayman KY1-2020<br>
    Cayman Islands
  </address>

  <ul class="contact-list">
    <li>
      <svg class="contact-icon" viewBox="0 0 14 14" aria-hidden="true"><rect x="4" y="1" width="6" height="12" rx="1" fill="#fff"/><rect x="5" y="3" width="4" height="5" fill="var(--red)"/></svg>
      : (345) 555-0142
    </li>
    <li>
      <svg class="contact-icon" viewBox="0 0 14 14" aria-hidden="true"><rect x="1" y="6" width="12" height="7" rx="1" fill="#fff"/><path d="M2 6 Q7 0 12 6" fill="none" stroke="#fff" stroke-width="2"/><circle cx="7" cy="9.5" r="1.5" fill="var(--red)"/></svg>
      : (345) 555-0143
    </li>
    <li>
      <svg class="contact-icon" viewBox="0 0 14 14" aria-hidden="true"><rect x="1" y="3" width="12" height="9" fill="#fff"/><path d="M1 3 L7 8 L13 3" fill="none" stroke="var(--red)" stroke-width="1.2"/></svg>
      : marcus@seabright.ky
    </li>
    <li>
      <svg class="contact-icon" viewBox="0 0 14 14" aria-hidden="true"><g fill="none" stroke="#fff" stroke-width="1"><circle cx="7" cy="7" r="6"/><ellipse cx="7" cy="7" rx="2.5" ry="6"/><line x1="1" y1="7" x2="13" y2="7"/></g></svg>
      : www.seabright.ky
    </li>
  </ul>
</section>

</body>
</html>
```